Career Development Skills | Business Card & Logo Design

We are looking for a business card including logo design for a new Sydney based business called 'Your Careerwise'.
We offer a range of services that focus on building the Employability or Employment skills for individuals focusing on job seekers and those interested in building skills required to develop their career. Employability skills are required not only to gain employment, but also to progress within an organisation so as to achieve one's potential.
Target Market(s)
Our client targets include corporates and govt agencies looking to build skills within their current employee base or assist staff in the transition between roles or workplaces.
Industry/Entity Type
Business
Look and feel

```html
<!DOCTYPE html>
<html lang="en">
<head>
<meta charset="utf-8">
<title>Your Careerwise – Business Card</title>
<link rel="stylesheet" href="https://fonts.googleapis.com/css2?family=Questrial&display=swap">
<style>
  :root {
    --navy-dark: #231f5c;
    --navy-mid: #28307e;
    --navy-light: #2c3b98;
    --white: #ffffff;
    --ink: #2a2a2a;
    --rule: #8a8a8a;
    --tile-border: #c9c9cf;
    --page: #ffffff;
  }
  html, body {
    margin: 0;
    padding: 0;
    overflow: hidden;
    background: var(--page);
  }
  .canvas {
    position: relative;
    width: 1200px;
    height: 900px;
    overflow: hidden;
    background: var(--page);
    font-family: "Questrial", "Century Gothic", sans-serif;
  }
  .card {
    position: absolute;
    top: 184px;
    width: 294px;
    height: 532px;
  }
  .card--front {
    left: 214px;
    background: linear-gradient(180deg, var(--navy-dark) 0%, var(--navy-mid) 50%, var(--navy-light) 100%);
  }
  .card--back {
    left: 694px;
  }
  .card__shape {
    position: absolute;
    inset: 0;
    width: 100%;
    height: 100%;
  }
  .contact {
    position: absolute;
    left: 42px;
    color: var(--ink);
    font-size: 14px;
    line-height: 19px;
  }
  .contact--identity { top: 60px; }
  .contact--reach { top: 206px; }
  .contact__name {
    display: inline-block;
    font-size: 17px;
    line-height: 20px;
    padding-right: 18px;
    border-bottom: 1px solid var(--rule);
    margin-bottom: 2px;
  }
  .brand {
    position: absolute;
    display: flex;
    align-items: center;
    color: var(--white);
  }
  .brand__tile {
    background: var(--white);
    border: 2px solid var(--tile-border);
    border-radius: 12px;
    box-sizing: border-box;
  }
  .brand--front {
    left: 16px;
    top: 442px;
    gap: 10px;
  }
  .brand--front .brand__tile {
    width: 66px;
    height: 66px;
  }
  .brand--front .brand__name {
    font-size: 22px;
    white-space: nowrap;
  }
  .brand__tile--back {
    position: absolute;
    left: 112px;
    top: 362px;
    width: 100px;
    height: 102px;
    border-radius: 16px;
  }
  .brand__name--back {
    position: absolute;
    left: 142px;
    top: 66px;
    height: 290px;
    writing-mode: vertical-rl;
    transform: rotate(180deg);
    text-align: center;
    color: var(--white);
    font-size: 32px;
    line-height: 40px;
    white-space: nowrap;
  }
</style>
</head>
<body>
<main class="canvas">
  <section class="card card--front" aria-label="Business card front">
    <svg class="card__shape" viewBox="0 0 294 532" aria-hidden="true">
      <polygon points="22,0 246,0 246,322 22,298" fill="#ffffff"/>
    </svg>
    <div class="contact contact--identity">
      <div class="contact__name">Mara Quell</div>
      <div>Harbour Lane</div>
      <div>20456</div>
    </div>
    <div class="contact contact--reach">
      <div>+61 555 018</div>
      <div>mara@yourcareerwise.com</div>
      <div>www.yourcareerwise.com</div>
    </div>
    <div class="brand brand--front">
      <span class="brand__tile"></span>
      <span class="brand__name">Your Careerwise</span>
    </div>
  </section>

  <section class="card card--back" aria-label="Business card back">
    <svg class="card__shape" viewBox="0 0 294 532" aria-hidden="true">
      <defs>
        <linearGradient id="backNavy" x1="0" y1="0" x2="0" y2="1">
          <stop offset="0" stop-color="#231f5c"/>
          <stop offset="0.5" stop-color="#28307e"/>
          <stop offset="1" stop-color="#2c3b98"/>
        </linearGradient>
      </defs>
      <path d="M6,0 L294,0 L294,532 L2,532 Q138,266 6,0 Z" fill="url(#backNavy)"/>
    </svg>
    <span class="brand__name--back">Your Careerwise</span>
    <span class="brand__tile brand__tile--back"></span>
  </section>
</main>
</body>
</html>
```